Entertainment Sound and Lighting company Business card

We need a professional looking business card designed for my growing entertainment sound and lighting company based in Sydney, Australia called "Kestrel Sound"

We provide technical production services (sound systems/lighting/vision) for events ranging from band gigs, weddings, corporate functions etc.

The business card needs to contain the following information:

Bartholomew Quenneville
Audio Engineer
Phone: 0478 615 702
Email: bartholomew@kestrelsound.com.au
Website: www.kestrelsound.com.au

Business logo has been attached in .ai format, please contact me if you need me to provide other files.

Target Market(s)

We need a business card that reflects our modern and professional company but still looks professional to appeal to our corporate clients.
We have a very broad target market spanning from bands needing PA systems for their gigs (18-30yrs) to event companies needing sound and lighting for weddings and other functions.

Industry/Entity Type

Business

Requirements
Must have
• Needs to include the logo that is attached of course, and the colour scheme.
Nice to have
• - Double sided

```html
<!DOCTYPE html>
<html lang="en">
<head>
<meta charset="utf-8">
<title>Kestrel Sound – Business Card</title>
<link rel="stylesheet" href="https://fonts.googleapis.com/css2?family=Cinzel:wght@400;600&display=swap">
<style>
  :root {
    --page: #ffffff;
    --frame: #1f8ed8;
    --card: #000000;
    --ink: #ffffff;
    --brand: #37c4e8;
  }
  * { margin: 0; padding: 0; box-sizing: border-box; }
  html, body {
    width: 1200px;
    height: 901px;
    overflow: hidden;
    background: var(--page);
  }
  .canvas {
    position: relative;
    width: 1200px;
    height: 901px;
    font-family: "Cinzel", serif;
  }
  .presentation-frame {
    position: absolute;
    left: 4px; top: 4px; right: 4px; bottom: 4px;
    border: 4px solid var(--frame);
    border-radius: 28px;
  }
  .card {
    position: absolute;
    width: 533px;
    height: 317px;
    background: var(--card);
  }
  .card--front { left: 159px; top: 94px; }
  .card--back { left: 552px; top: 474px; }

  .brand {
    display: flex;
    align-items: center;
    justify-content: center;
    gap: 0.4em;
    color: var(--brand);
    font-weight: 600;
    white-space: nowrap;
  }
  .brand__dot {
    width: 0.55em;
    height: 0.55em;
    border-radius: 50%;
    background: var(--brand);
  }
  .card--front .brand {
    position: absolute;
    left: 0; right: 0; top: 128px;
    font-size: 50px;
    letter-spacing: 1px;
  }

  .contact {
    position: absolute;
    inset: 0;
    color: var(--ink);
    text-align: center;
  }
  .contact__name {
    position: absolute; left: 0; right: 0; top: 36px;
    font-size: 24px; font-weight: 600; letter-spacing: 2px;
  }
  .contact__role {
    position: absolute; left: 0; right: 0; top: 66px;
    font-size: 13px; letter-spacing: 1.5px;
  }
  .contact__email {
    position: absolute; left: 0; right: 0; top: 118px;
    font-size: 14px; letter-spacing: 1.5px;
  }
  .contact__phone {
    position: absolute; left: 0; right: 0; top: 150px;
    font-size: 18px; letter-spacing: 1.5px;
  }
  .contact__phone-label { font-size: 12px; margin-right: 6px; }
  .card--back .brand {
    position: absolute; left: 0; right: 0; top: 212px;
    font-size: 22px;
  }
  .contact__web {
    position: absolute; left: 0; right: 0; top: 272px;
    font-size: 15px; letter-spacing: 2px;
  }
</style>
</head>
<body>
<main class="canvas">
  <div class="presentation-frame"></div>

  <section class="card card--front" aria-label="Business card front">
    <div class="brand"><span class="brand__dot"></span>Kestrel Sound</div>
  </section>

  <section class="card card--back" aria-label="Business card back">
    <div class="contact">
      <p class="contact__name">Bartholomew Quenneville</p>
      <p class="contact__role">Audio Engineer</p>
      <p class="contact__email">bartholomew@kestrelsound.com.au</p>
      <p class="contact__phone"><span class="contact__phone-label">Phone</span>0478 615 702</p>
      <div class="brand"><span class="brand__dot"></span>Kestrel Sound</div>
      <p class="contact__web">www.kestrelsound.com.au</p>
    </div>
  </section>
</main>
</body>
</html>
```